Surgical Sales Presentation Folder

Presentation folder; three panel; custom cutouts; Six 8.5 x 11 full color sales sheets to be bound into presentation folder; 5 full color sales sheets, stepped, longest being 8.5 x 11.
We are Kelvar Surgical Group and we are a surgical company that supports physicians who wish to become surgeons. Our clients are Physicians. As such, the design needs to be very professional.
I have included a list of photos and a letter describing what we like about each photo. I have included the verbiage with page identifiers. If this makes scene, please feel free to add photos to the inside of the folder or I can provide you with examples that we think are similar to what we are looking for.
Updates
Target Market(s)
Doctors who want to be surgeons.
Industry/Entity Type
Sales
Requirements
Must have
- Presentation folder; three panel; custom cutouts; Six 8.5 x 11 full color sales sheets to be bound into presentation folder; 5 full color sales sheets, stepped, longest being 8.5 x 11.

```html
<!DOCTYPE html>
<html lang="en">
<head>
<meta charset="utf-8">
<title>Kelvar Surgical Group – Presentation Folder</title>
<link rel="stylesheet" href="https://fonts.googleapis.com/css2?family=Nunito:wght@600;700;800&family=Crimson+Text:ital@0;1&family=Arimo:wght@700&display=swap">
<style>
  :root {
    --backdrop: #5b3320;
    --label: #d9ccb8;
    --sheet-blue: #1c8fc9;
    --sheet-band: #1b95cf;
    --sheet-white: #ffffff;
    --headline-red: #c0392b;
    --body-ink: #3a3a3a;
    --accent-red: #b8322a;
    --brand-navy: #123f7a;
  }
  * { box-sizing: border-box; margin: 0; padding: 0; }
  html, body { width: 1200px; height: 1000px; overflow: hidden; }
  body { background: var(--backdrop); position: relative; font-family: "Nunito", sans-serif; }

  .sheet { position: absolute; box-shadow: 0 3px 8px rgba(0,0,0,.35); }

  .quote-sheet {
    left: 58px; top: 40px; width: 410px; height: 230px;
    background: var(--sheet-blue); transform: rotate(-4deg);
    color: var(--sheet-white);
  }
  .quote-mark { position: absolute; font: 800 72px/1 "Nunito", sans-serif; }
  .quote-mark.open { left: 40px; top: 62px; }
  .quote-mark.close { right: 10px; top: 118px; }
  .quote-text {
    position: absolute; left: 100px; top: 52px;
    font: 700 13.5px/19px "Nunito", sans-serif; white-space: nowrap;
  }
  .quote-author {
    position: absolute; left: 180px; top: 150px;
    font: italic 15px "Crimson Text", serif;
  }

  .article-sheet {
    left: 468px; top: 22px; width: 390px; height: 250px;
    background: var(--sheet-white); transform: rotate(2deg);
  }
  .article-band { position: absolute; left: 0; top: 0; right: 0; height: 44px; background: var(--sheet-band); }
  .article-headline {
    position: absolute; left: 20px; top: 44px; width: 190px; height: 116px;
    background: var(--headline-red); color: var(--sheet-white);
    padding: 20px 6px 0 10px;
    font: 700 17px/1.15 "Nunito", sans-serif; white-space: nowrap;
  }
  .article-photo {
    position: absolute; left: 210px; top: 44px; width: 180px; height: 116px;
    background: linear-gradient(135deg, #c9d6e2, #7c91a8 60%, #4f6479);
  }
  .article-kicker {
    position: absolute; left: 22px; top: 164px;
    font: italic 10px "Crimson Text", serif; color: var(--accent-red);
  }
  .article-body {
    position: absolute; left: 22px; top: 176px; width: 340px;
    column-count: 2; column-gap: 16px;
    font: 10px/1.3 "Crimson Text", serif; color: var(--body-ink); text-align: justify;
  }

  .folder { position: absolute; left: 52px; top: 200px; width: 1084px; height: 528px; filter: drop-shadow(0 4px 6px rgba(0,0,0,.45)); }

  .brand-name { font-family: "Nunito", sans-serif; font-weight: 800; fill: var(--brand-navy); }

  .panel-label {
    position: absolute; top: 762px;
    font: 700 46px "Arimo", sans-serif; color: var(--label);
  }
  .panel-label.back { left: 205px; }
  .panel-label.front { left: 597px; }
</style>
</head>
<body>

  <article class="sheet quote-sheet">
    <span class="quote-mark open">“</span>
    <p class="quote-text">In the mid-20th Century, physicians were<br>the pillars of any community. If you were<br>smart, sincere and ambitious, there was<br>nothing nobler or more rewarding that<br>you could aspire to become.</p>
    <span class="quote-author">— Marlen Osterby</span>
    <span class="quote-mark close">”</span>
  </article>

  <article class="sheet article-sheet">
    <div class="article-band"></div>
    <h2 class="article-headline">So What Is It<br>Like To Be A Hair<br>Transplant Surgeon?</h2>
    <div class="article-photo" role="img" aria-label="Photo of surgical instruments on a tray"></div>
    <span class="article-kicker">Surgical Hours</span>
    <p class="article-body">Your day as a hair transplant surgeon begins early, with calm planning before transplant surgery starts.</p>
  </article>

  <svg class="folder" viewBox="0 0 1084 528" aria-label="Presentation folder back, front and flap">
    <defs>
      <linearGradient id="folderBase" x1="0" y1="0" x2="0" y2="1">
        <stop offset="0" stop-color="#3f86cf"/>
        <stop offset=".5" stop-color="#6cb6e8"/>
        <stop offset="1" stop-color="#86cdf2"/>
      </linearGradient>
      <linearGradient id="waveDeep" x1="0" y1="0" x2="1" y2="1">
        <stop offset="0" stop-color="#1c56a6"/>
        <stop offset="1" stop-color="#2d78c8"/>
      </linearGradient>
      <linearGradient id="peakLight" x1="0" y1="0" x2="0" y2="1">
        <stop offset="0" stop-color="#ffffff"/>
        <stop offset="1" stop-color="#9fd6f4"/>
      </linearGradient>
      <clipPath id="folderShape">
        <path d="M0 0 H820 A264 264 0 0 1 820 528 H0 Z"/>
      </clipPath>
    </defs>
    <g clip-path="url(#folderShape)">
      <rect width="1084" height="528" fill="url(#folderBase)"/>
      <path d="M0 110 C140 20 330 -8 560 -20 L0 -20 Z" fill="url(#waveDeep)"/>
      <path d="M0 130 C140 40 330 8 580 -10" fill="none" stroke="#a9dcf7" stroke-width="2" opacity=".7"/>
      <path d="M0 420 C180 490 420 500 660 540 L0 540 Z" fill="#5fb4e6" opacity=".8"/>
      <path d="M0 455 C170 472 380 480 620 540" fill="none" stroke="#ffffff" stroke-width="1.5" opacity=".7"/>
      <path d="M400 528 C600 470 760 300 820 200 C880 300 980 400 1084 430 L1084 528 Z" fill="url(#waveDeep)"/>
      <path d="M440 528 C620 430 760 260 820 65 C860 200 940 330 1084 390 L1084 440 C980 400 880 310 820 210 C740 340 600 480 460 528 Z" fill="#2a6fc0"/>
      <path d="M380 528 C600 420 760 250 820 65" fill="none" stroke="#d6f0ff" stroke-width="2"/>
      <path d="M500 528 C650 440 770 320 820 200 C860 300 950 380 1084 440 L1084 470 C950 420 870 360 820 330 C740 420 640 500 560 528 Z" fill="url(#peakLight)" opacity=".85"/>
      <path d="M560 528 C680 470 770 400 820 380 C880 410 980 450 1084 470 L1084 528 Z" fill="#1d5ba8"/>
      <rect x="820" y="0" width="264" height="528" fill="#0b2f63" opacity=".18"/>
      <line x1="410" y1="0" x2="410" y2="528" stroke="#2b6cb3" stroke-width="1" opacity=".6"/>
      <line x1="820" y1="0" x2="820" y2="528" stroke="#2b6cb3" stroke-width="1" opacity=".5"/>
      <circle cx="154" cy="443" r="7" fill="#123f7a"/>
      <text class="brand-name" x="166" y="448" font-size="13">Kelvar Surgical Group</text>
      <circle cx="704" cy="353" r="6" fill="#123f7a"/>
      <text class="brand-name" x="714" y="357" font-size="11">Kelvar Surgical Group</text>
    </g>
  </svg>

  <span class="panel-label back">Back</span>
  <span class="panel-label front">Front</span>

</body>
</html>
```